Website for boutique digital agency helping high-tech startups accelerate growth.

We need a website design for a relatively young company based in Mauritius called 'LoomTrax'.

We are a professional services firm delivering digital infrastructure for revenue operations (RevOps)*.

Entrepreneurial startups and SMBs in the technology sector work with us to accelerate growth by delivering extraordinary customer experiences across the full customer lifecycle.

We would like a colourful design that utilises the (4) colours of our existing logo design.

The final design should communicate dynamic growth through relentless customer focus.
----------------------------------------------------------
*Revenue Operations (RevOps) is the strategic alignment of sales, marketing and customer success operations to accelerate growth by delivering extraordinary customer experiences across the full customer life cycle.
Updates

Target Market(s)

Entrepreneurial startups and SMBs (Small/Medium Businesses) in the technology sector.

Question: Why the technology sector?

Answer: Because technology entrepreneurs often have a tremendous challenge to effectively communicate to the market and to prospective customers the value and the benefits of their products & services due to the inherent complexity of technological innovation.

LoomTrax is a team of creatively-minded engineers and technologists who have worked with and understand the technologies and innovations our clients are passionate about bringing to market.

Industry/Entity Type

Professional Service

Number of Pages Required

5+ page

Font styles to use
Sans Serif

Requirements
Must have
• Minimalistic designs rich with visual meaning are highly preferred. Mobile responsive designs are also required. Must show how designs render on Desktop, Tablet and Smartphone devices.

Website pages:
1) Homepage: problem statement, target customers, value proposition & benefits
2) Services: 3-4 tiers of services packages with pricing and "how to work with us"
3) Resources: links to all kinds of relevant materials
4) Contact Us: contact form and special project quote form
5) Blog: matrix design with featured images for each post
Nice to have
• Bold, interesting, colourful, inspiring images that visually communicate:
- relentless customer focus
- extraordinary, memorable experiences
- business at the speed of innovation
Should not have
• Any meme or theme that panders to "political correctness".

```html
<!DOCTYPE html>
<html lang="en">
<head>
<meta charset="UTF-8">
<title>LoomTrax – RevOps Aligns Everyone</title>
<link rel="stylesheet" href="https://fonts.googleapis.com/css2?family=Jost:wght@400;500;600&display=swap">
<style>
  :root {
    --ink: #27343b;
    --green: #80c31f;
    --green-faint: #e1efcd;
    --teal: #16807a;
    --red: #ff0a3c;
    --orange: #ff6a0a;
    --paper: #ffffff;
  }
  * { margin: 0; padding: 0; box-sizing: border-box; }
  html, body {
    width: 1200px; height: 675px; overflow: hidden;
    background: var(--paper);
    font-family: "Jost", sans-serif;
    color: var(--ink);
  }
  .page { position: relative; width: 1200px; height: 675px; overflow: hidden; }

  .accent-band {
    position: absolute;
    border-radius: 26px;
    opacity: 0.85;
  }
  .accent-band--top {
    left: 349px; top: -20px; width: 145px; height: 70px;
    background: linear-gradient(120deg, var(--green), var(--teal) 55%, var(--red));
  }
  .accent-band--bottom {
    left: 390px; top: 624px; width: 128px; height: 72px;
    background: linear-gradient(120deg, var(--green), var(--teal) 50%, var(--orange));
  }

  .brand {
    position: absolute; left: 88px; top: 46px;
    display: flex; align-items: center; gap: 8px;
    font-size: 22px; font-weight: 600; color: var(--ink);
    letter-spacing: 0.3px;
  }
  .brand-dot { width: 10px; height: 10px; border-radius: 50%; background: var(--red); }

  .main-nav { position: absolute; top: 51px; left: 696px; display: flex; gap: 31px; }
  .main-nav a {
    font-size: 17px; color: var(--ink); text-decoration: none;
    letter-spacing: 0.4px; padding-bottom: 3px;
  }
  .main-nav a.is-active { border-bottom: 1.5px solid var(--ink); }

  .section-index {
    position: absolute; left: 68px; top: 274px;
    font-size: 32px; font-weight: 600; line-height: 1; color: var(--green-faint);
  }
  .section-nav { position: absolute; left: 117px; top: 236px; }
  .section-nav a {
    display: block; position: absolute; left: 0; white-space: nowrap;
    font-size: 17.5px; color: var(--ink); text-decoration: none; letter-spacing: 0.5px;
  }
  .section-nav a.is-current { font-size: 23.5px; font-weight: 600; letter-spacing: 0.8px; }

  .hero { position: absolute; left: 405px; top: 214px; width: 350px; }
  .hero-title { font-size: 33px; font-weight: 600; line-height: 38px; letter-spacing: 0.6px; }
  .hero-text { margin-top: 8px; font-size: 17.5px; line-height: 18.75px; letter-spacing: 0.4px; }
  .hero-button {
    display: flex; align-items: center; justify-content: center;
    margin-top: 32px; width: 163px; height: 51px; border-radius: 11px;
    background: var(--green); color: var(--paper);
    font-size: 17.5px; font-weight: 500; text-decoration: none; letter-spacing: 0.3px;
  }

  .hero-visual {
    position: absolute; left: 810px; top: 228px; width: 270px; height: 220px;
    border-radius: 50%;
    background: radial-gradient(circle at 50% 52%, var(--green) 0, #8fcf2e 45%, rgba(128,195,31,0) 72%);
  }
</style>
</head>
<body>
<div class="page">
  <div class="accent-band accent-band--top" role="img" aria-label="Decorative diagonal stripes in green, teal and red"></div>
  <div class="accent-band accent-band--bottom" role="img" aria-label="Decorative diagonal stripes in green, orange, teal and red"></div>

  <div class="brand"><span class="brand-dot"></span>LoomTrax</div>

  <nav class="main-nav">
    <a href="#" class="is-active">Home</a>
    <a href="#">Services</a>
    <a href="#">Resources</a>
    <a href="#">Contact Us</a>
    <a href="#">Blog</a>
  </nav>

  <div class="section-index">02</div>
  <nav class="section-nav">
    <a href="#" style="top:3px">Home</a>
    <a href="#" class="is-current" style="top:45px">Problem Statement</a>
    <a href="#" style="top:94px">Target Customers</a>
    <a href="#" style="top:135px">Value Proposition</a>
    <a href="#" style="top:176px">Benefits</a>
  </nav>

  <section class="hero">
    <h1 class="hero-title">RevOps Aligns<br>Everyone</h1>
    <p class="hero-text">RevOps keeps Marketing, Sales, and<br>Customer Success aligned around the<br>customer – unifying metrics, tech ownership,<br>and change management.</p>
    <a href="#" class="hero-button">Learn More</a>
  </section>

  <div class="hero-visual" role="img" aria-label="Illustration of a green globe with an orbit ring and pink location pins spread across it"></div>
</div>
</body>
</html>
```